New web page design for our brand Casa Lunares

We have changed our logo and the image of our products, so we would like to redesign ,our web page as well according to the new design.
Our cosmetic products are based in nature and tradition, like they used to be prepared in the old pharmacies.
Our actual web is www.casalunaresweb.es, so we need similar estructure but completely different design.

Industry/Entity Type

Cosmetics

Number of Pages Required

5+ page

Requirements
Must have
• References to natural ingredients and also to old pharmacys or apothecaries.
Nice to have
• Nature images or old botanics drawings
• I would like to have a cover page with just an image saying welcome to Casa Lunares's world

```html
<!DOCTYPE html>
<html lang="es">
<head>
<meta charset="utf-8">
<title>Casa Lunares</title>
<link href="https://fonts.googleapis.com/css2?family=Lato:wght@300;400;700;900&display=swap" rel="stylesheet">
<style>
:root{
  --brown:#3a2623;
  --brown-deep:#2c1c1a;
  --orange:#f2a81d;
  --white:#ffffff;
  --paper:#f3f1ef;
  --ink:#3b2a27;
  --muted:#8a7f7c;
  --line:#e2dedc;
}
*{box-sizing:border-box;margin:0;padding:0}
html,body{width:1200px;height:3844px;overflow:hidden}
body{font-family:'Lato',sans-serif;color:var(--ink);background:var(--white);position:relative}
a{color:inherit;text-decoration:none}

/* header */
.site-header{position:absolute;top:0;left:0;width:1200px;height:64px;z-index:5}
.brand{position:absolute;left:100px;top:0;width:150px;height:180px;background:var(--white);display:flex;flex-direction:column;align-items:center;justify-content:center;gap:12px;box-shadow:0 2px 8px rgba(0,0,0,.15)}
.brand-dot{width:22px;height:22px;border-radius:50%;background:var(--brown)}
.brand-name{font-weight:700;font-size:20px;color:var(--brown);text-align:center;line-height:1.2}
.main-nav{position:absolute;right:0;top:0;height:64px;width:700px;background:var(--white);display:flex;justify-content:center;align-items:stretch}
.main-nav a{display:flex;align-items:center;padding:0 22px;font-size:15px;font-weight:700;color:var(--ink);letter-spacing:.5px}
.main-nav a.active{background:var(--orange);color:var(--white)}

/* hero */
.hero{position:absolute;top:0;left:0;width:1200px;height:660px;background:var(--brown)}
.hero-photo{position:absolute;right:0;top:0;width:600px;height:660px;background:linear-gradient(110deg,var(--brown) 0%,#6b4a40 35%,#c8a391 70%,#e8d3c6 100%)}
.hero-title{position:absolute;left:120px;top:260px;width:360px;color:var(--white);text-align:center}
.hero-title .kicker{display:block;font-size:22px;font-weight:700;letter-spacing:2px}
.hero-title .headline{display:block;margin-top:8px;font-size:56px;font-weight:900;color:var(--orange);letter-spacing:2px;line-height:1.05}
.hero-title .sub{display:block;margin-top:6px;font-size:26px;font-weight:700;letter-spacing:3px}
.hero-lead{position:absolute;left:150px;top:500px;width:300px;color:var(--white);font-size:14px;line-height:1.6;text-align:center;font-weight:300}

/* section heads */
.section-head{text-align:center}
.section-head h2{font-size:44px;font-weight:900;letter-spacing:1px;color:var(--ink)}
.rule{display:block;margin:14px auto 0;width:90px;height:2px;background:var(--ink)}
.section-head p{margin:30px auto 0;width:540px;font-size:15px;line-height:1.6;color:var(--muted)}
.products-intro{position:absolute;top:700px;left:0;width:1200px}

/* lines */
.line-band{position:absolute;left:0;width:1200px;height:440px;display:flex}
.line-band .panel{width:600px;height:440px;background:var(--brown);color:var(--white);padding:50px 80px 0;text-align:center}
.line-band .photo{width:600px;height:440px}
.panel h3{font-size:32px;font-weight:900;letter-spacing:1px}
.panel .rule{background:var(--white);margin-top:12px}
.panel p{margin-top:28px;font-size:14px;line-height:1.7;text-align:left;font-weight:300}
.btn{display:inline-block;background:var(--orange);color:var(--brown);font-size:13px;font-weight:700;padding:14px 30px;letter-spacing:.5px}
.panel .btn{margin-top:34px}
.premium{top:960px}
.premium .photo{background:linear-gradient(135deg,#d9c2a8,#a98a6c 60%,#e7dccd)}
.children{top:1400px}
.children .photo{background:linear-gradient(135deg,#efe6e2,#dcc6bd 55%,#f6efec)}
.featured-intro{position:absolute;top:1910px;left:0;width:1200px}

/* cards */
.card-grid{position:absolute;top:2150px;left:100px;width:1000px;display:grid;grid-template-columns:repeat(3,320px);column-gap:20px;row-gap:140px}
.card{height:330px;background:var(--paper);text-align:center;border:1px solid var(--line)}
.card .thumb{height:160px;background:linear-gradient(180deg,#ffffff,#e9e3df)}
.card h4{margin-top:24px;font-size:17px;font-weight:900;letter-spacing:.5px;line-height:1.2}
.card p{margin:12px auto 0;width:250px;font-size:12px;line-height:1.5;color:var(--muted)}
.card .btn{margin-top:16px;background:var(--brown);color:var(--white);padding:10px 26px;font-size:12px}
.card.highlight{background:var(--brown);color:var(--white)}
.card.highlight h4{margin-top:18px}
.card.highlight p{color:#d6ccc9;margin-top:8px}
.card.highlight .btn{background:var(--orange);color:var(--brown);margin-top:10px}

/* newsletter */
.newsletter{position:absolute;top:3040px;left:0;width:1200px;height:200px;background:var(--orange);display:flex;align-items:center;padding:0 100px}
.newsletter h2{font-size:34px;font-weight:900;color:var(--brown);width:430px}
.newsletter .field{width:360px;height:50px;background:var(--white);opacity:.55;font-size:13px;color:var(--muted);display:flex;align-items:center;padding-left:18px}
.newsletter .submit{margin-left:40px;width:170px;height:50px;background:var(--brown);color:var(--white);font-weight:700;font-size:14px;display:flex;align-items:center;justify-content:center}

/* footer */
.site-footer{position:absolute;top:3240px;left:0;width:1200px;height:540px;background:var(--brown);color:var(--white);display:grid;grid-template-columns:260px 260px 260px 220px;padding:60px 100px 0}
.site-footer h5{font-size:18px;font-weight:900;letter-spacing:.5px;margin-bottom:22px}
.site-footer p{font-size:13px;line-height:1.7;color:#d8cdca;width:220px;font-weight:300}
.foot-list{list-style:none}
.foot-list li{font-size:13px;color:#d8cdca;margin-bottom:28px}
.social li{display:flex;align-items:center;gap:18px;margin-bottom:30px}
.social .sq{width:40px;height:40px;background:var(--white);opacity:.9}
.contact .input{height:34px;background:var(--white);margin-bottom:18px;width:220px}
.contact .area{height:80px}
.contact .send{width:220px;height:38px;background:var(--orange);color:var(--brown);font-size:12px;font-weight:700;display:flex;align-items:center;justify-content:center;margin-top:8px}
.contact p{margin-bottom:18px}
.copyright{position:absolute;top:3780px;left:0;width:1200px;height:64px;background:var(--brown-deep);color:#d8cdca;font-size:13px;display:flex;align-items:center;justify-content:center}
</style>
</head>
<body>

<header class="site-header">
  <a class="brand" href="#"><span class="brand-dot"></span><span class="brand-name">Casa<br>Lunares</span></a>
  <nav class="main-nav">
    <a class="active" href="#">LAB</a>
    <a href="#">PRODUCT LINES</a>
    <a href="#">SERVICES</a>
    <a href="#">NEWS</a>
    <a href="#">CONTACT</a>
    <a href="#">SHOP</a>
  </nav>
</header>

<section class="hero">
  <div class="hero-photo" role="img" aria-label="Portrait of a woman with a white flower in her hair"></div>
  <h1 class="hero-title">
    <span class="kicker">CUIDA TU PIEL</span>
    <span class="headline">NATURAL</span>
    <span class="sub">CADA DÍA</span>
  </h1>
  <p class="hero-lead">Descubre nuestros productos naturales elaborados con la tradición de las antiguas boticas, para cuidar tu piel cada día con la pureza de la naturaleza.</p>
</section>

<section class="products-intro section-head">
  <h2>OUR PRODUCTS</h2>
  <span class="rule"></span>
  <p>Develop new lines of cleansers, soft nutrient products and creams, which provide effective beauty and growth.</p>
</section>

<section class="line-band premium">
  <div class="panel">
    <h3>PREMIUM LINE</h3>
    <span class="rule"></span>
    <p>Inspired by old apothecary recipes, our premium line combines the finest natural ingredients with gentle care for the skin. Each formula is prepared in small batches, rich in botanical oils and extracts that nourish, soothe and restore your daily natural beauty.</p>
    <a class="btn" href="#">SEE MORE</a>
  </div>
  <div class="photo" role="img" aria-label="Young woman with a flower crown in soft light"></div>
</section>

<section class="line-band children">
  <div class="photo" role="img" aria-label="Sleeping baby wearing a flower garland"></div>
  <div class="panel">
    <h3>CHILDREN LINE</h3>
    <span class="rule"></span>
    <p>Our children line is specially formulated for the needs of the youngest skin. Mild plant based care, free of harsh additives, to protect the delicate and soft skin of babies.</p>
    <a class="btn" href="#">SEE MORE</a>
  </div>
</section>

<section class="featured-intro section-head">
  <h2>FEATURED PRODUCTS</h2>
  <span class="rule"></span>
  <p>Develop new lines of cleansers, soft nutrient products and creams, which provide effective beauty and growth.</p>
</section>

<section class="card-grid">
  <article class="card">
    <div class="thumb" role="img" aria-label="Natural care bottles with flowers"></div>
    <h4>NATURAL CARE</h4>
    <p>Gentle formulas made with pure plant oils and extracts for a clean daily routine.</p>
    <a class="btn" href="#">SEE MORE</a>
  </article>
  <article class="card highlight">
    <div class="thumb" role="img" aria-label="Pharmaceutical cream tubes and bottle"></div>
    <h4>LINE RECOMMENDATION<br>PHARMACEUTICAL</h4>
    <p>Products recommended by pharmacists for sensitive and demanding skin.</p>
    <a class="btn" href="#">SEE MORE</a>
  </article>
  <article class="card">
    <div class="thumb" role="img" aria-label="Jar of body cream"></div>
    <h4>BODY TREATMENT</h4>
    <p>Rich creams and balms that hydrate, soften and protect the whole body.</p>
    <a class="btn" href="#">SEE MORE</a>
  </article>
  <article class="card">
    <div class="thumb" role="img" aria-label="Family care bottles"></div>
    <h4>FAMILY HEALTH</h4>
    <p>Everyday care for all the family, with mild ingredients from nature.</p>
    <a class="btn" href="#">SEE MORE</a>
  </article>
  <article class="card">
    <div class="thumb" role="img" aria-label="Nail care bottles"></div>
    <h4>NAIL TREATMENT</h4>
    <p>Strengthening treatments with natural oils to care for healthy nails.</p>
    <a class="btn" href="#">SEE MORE</a>
  </article>
  <article class="card">
    <div class="thumb" role="img" aria-label="Aromatic spray bottles"></div>
    <h4>AROMATIC LINE</h4>
    <p>Fresh scents from herbs and flowers to awaken the senses every day.</p>
    <a class="btn" href="#">SEE MORE</a>
  </article>
</section>

<section class="newsletter">
  <h2>SIGN UP NEWSLETTER</h2>
  <div class="field">Enter your email address</div>
  <a class="submit" href="#">SUBSCRIBE</a>
</section>

<footer class="site-footer">
  <div>
    <h5>ABOUT US</h5>
    <p>Casa Lunares is a family workshop that prepares natural cosmetics following the tradition of old pharmacies, with carefully chosen ingredients and a slow, honest way of making each product for the care of your skin.</p>
  </div>
  <div>
    <h5>NAVIGATIONS</h5>
    <ul class="foot-list">
      <li>LAB</li><li>PRODUCT LINES</li><li>SERVICES</li><li>NEWS</li><li>CONTACT</li><li>SHOP</li>
    </ul>
  </div>
  <div>
    <h5>FOLLOW US</h5>
    <ul class="foot-list social">
      <li><span class="sq"></span>Journal</li>
      <li><span class="sq"></span>Community</li>
      <li><span class="sq"></span>Gallery</li>
      <li><span class="sq"></span>Videos</li>
    </ul>
  </div>
  <div class="contact">
    <h5>CONTACT US</h5>
    <p>Write us and we will answer you shortly.</p>
    <div class="input"></div>
    <div class="input"></div>
    <div class="input area"></div>
    <a class="send" href="#">SEND YOUR MESSAGE</a>
  </div>
</footer>
<div class="copyright">Copyright 2015 © Casa Lunares</div>

</body>
</html>
```